Business Card for Jewelry Business

We need a new namecard design for a jewelry company based in Bangkok, Thailand. We have a new website recently and want the new namecard to reflect our new modern image. I have uploaded our old namecard to show you the information that needs to be on the namecard. Pls check our website www.qelburn.com for the new color scheme to help design the new namecard.

```html
<!DOCTYPE html>
<html lang="en">
<head>
<meta charset="utf-8">
<title>Qelburn Manufacturers – Business Card</title>
<link rel="stylesheet" href="https://fonts.googleapis.com/css2?family=Bebas+Neue&family=Open+Sans:wght@400;600&display=swap">
<style>
  :root {
    --stage: #2a2a2a;
    --card: #121212;
    --teal: #52c4c9;
    --ink: #f2efe9;
    --muted: #d9d6d0;
    --fb: #3b5998;
    --ig: #d6336c;
  }
  * { margin: 0; padding: 0; box-sizing: border-box; }
  html, body { width: 1200px; height: 900px; overflow: hidden; }
  body {
    background: var(--stage);
    font-family: "Open Sans", Arial, sans-serif;
    color: var(--ink);
    position: relative;
  }
  .card {
    position: absolute;
    left: 290px;
    width: 620px;
    height: 354px;
    background: var(--card);
    box-shadow: 0 12px 30px rgba(0,0,0,.55);
    overflow: hidden;
  }
  .card--front { top: 60px; }
  .card--back { top: 486px; }
  .card__band {
    position: absolute;
    left: 0; right: 0; bottom: 0;
    height: 14px;
    background: var(--teal);
  }

  /* Front */
  .wordmark {
    position: absolute;
    left: 0; right: 0; top: 130px;
    display: flex;
    align-items: center;
    justify-content: center;
    gap: 18px;
  }
  .wordmark__dot {
    width: 54px; height: 54px;
    border-radius: 50%;
    background: var(--teal);
  }
  .wordmark__name {
    font-size: 38px;
    font-weight: 400;
    letter-spacing: 6px;
    line-height: 1.1;
    color: var(--ink);
    text-transform: uppercase;
  }
  .wordmark__name small {
    display: block;
    font-size: 13px;
    letter-spacing: 4px;
  }

  /* Back */
  .person {
    position: absolute;
    top: 34px; left: 0; right: 0;
    text-align: center;
  }
  .person__name {
    font-family: "Bebas Neue", Impact, sans-serif;
    font-size: 40px;
    letter-spacing: 1px;
    color: var(--teal);
    line-height: 1;
  }
  .person__title {
    font-size: 14px;
    color: var(--muted);
    margin-top: 4px;
  }
  .contact {
    position: absolute;
    top: 132px;
    right: 330px;
    list-style: none;
    text-align: right;
  }
  .contact li {
    display: flex;
    align-items: center;
    justify-content: flex-end;
    gap: 10px;
    font-size: 14px;
    line-height: 22px;
  }
  .contact svg { width: 14px; height: 14px; fill: none; stroke: var(--teal); stroke-width: 1.6; }
  .divider {
    position: absolute;
    top: 134px;
    left: 306px;
    width: 1.5px;
    height: 106px;
    background: var(--teal);
  }
  .address {
    position: absolute;
    top: 130px;
    left: 322px;
    font-style: normal;
    font-size: 14px;
    line-height: 21px;
  }
  .address__company { color: var(--teal); }
  .social {
    position: absolute;
    bottom: 32px;
    left: 0; right: 0;
    display: flex;
    justify-content: center;
    gap: 36px;
    font-size: 14px;
  }
  .social__item { display: flex; align-items: center; gap: 9px; }
  .social__mark { width: 18px; height: 18px; border-radius: 50%; }
  .social__mark--page { background: var(--fb); }
  .social__mark--photo { background: var(--ig); }
</style>
</head>
<body>

<section class="card card--front" aria-label="Card front">
  <div class="wordmark">
    <span class="wordmark__dot"></span>
    <span class="wordmark__name">Qelburn<small>Manufacturers</small></span>
  </div>
  <div class="card__band"></div>
</section>

<section class="card card--back" aria-label="Card back">
  <header class="person">
    <h1 class="person__name">Nara Siriwan</h1>
    <p class="person__title">Sales &amp; Product Development Manager</p>
  </header>

  <ul class="contact">
    <li>+662-418-2730-5
      <svg viewBox="0 0 16 16"><path d="M4 1.5l2.5 3-1.5 1.5a8 8 0 0 0 5 5l1.5-1.5 3 2.5-1.5 2.5C7 14.5 1.5 9 1.5 3z"/></svg></li>
    <li>+662-604-9183
      <svg viewBox="0 0 16 16"><rect x="4" y="1.5" width="8" height="4"/><rect x="1.5" y="5.5" width="13" height="6"/><rect x="4" y="9.5" width="8" height="5"/></svg></li>
    <li>nara@qelburn.com
      <svg viewBox="0 0 16 16"><rect x="1.5" y="3.5" width="13" height="9"/><path d="M1.5 3.5l6.5 5 6.5-5"/></svg></li>
    <li>hello@qelburn.com
      <svg viewBox="0 0 16 16"><rect x="1.5" y="3.5" width="13" height="9"/><path d="M1.5 3.5l6.5 5 6.5-5"/></svg></li>
    <li>http://www.qelburn.net
      <svg viewBox="0 0 16 16"><circle cx="8" cy="8" r="6.5"/><ellipse cx="8" cy="8" rx="3" ry="6.5"/><path d="M1.5 8h13"/></svg></li>
  </ul>

  <div class="divider"></div>

  <address class="address">
    <span class="address__company">Qelburn Manufacturers Co.,Ltd</span><br>
    218 Moo 7 Rattanakorn Road<br>
    Export Trade Zone 2<br>
    Bang Saphan Industrial Park<br>
    Nong Chok, Bangkok 10590 Thailand
  </address>

  <div class="social">
    <span class="social__item"><span class="social__mark social__mark--page"></span>Qelburn Manufacturers</span>
    <span class="social__item"><span class="social__mark social__mark--photo"></span>@QelburnMfr</span>
  </div>

  <div class="card__band"></div>
</section>

</body>
</html>
```